New Packaging Design Project

Wine packaging redesign. Retail partner requested a redesign of a private label wine. The old label is attached. Our partner liked the Lantern and Briar label and wanted something similar. There will be a logo added to the top of the label

Went on vacation/holiday

```html
<!DOCTYPE html>
<html lang="en">
<head>
<meta charset="utf-8">
<title>Napa Valley Red Blend 2018 Label</title>
<link rel="stylesheet" href="https://fonts.googleapis.com/css2?family=Cinzel:wght@400&family=Barlow+Semi+Condensed:wght@300;600&family=Cormorant+Garamond:wght@500&display=swap">
<style>
  :root {
    --label-stone: #7a7166;
    --title-gold: #f6d985;
    --varietal-sand: #cdbda3;
    --divider-ink: #4a4640;
    --ink-white: #ffffff;
    --landscape-dark: #4f4e47;
    --landscape-mid: #605c53;
  }
  html, body {
    margin: 0;
    padding: 0;
    width: 826px;
    height: 1200px;
    overflow: hidden;
    background: var(--label-stone);
  }
  .wine-label {
    position: relative;
    width: 826px;
    height: 1200px;
    background: var(--label-stone);
    overflow: hidden;
  }
  .region-title {
    position: absolute;
    top: 278px;
    left: 0;
    width: 100%;
    margin: 0;
    text-align: center;
    font-family: "Cinzel", serif;
    font-weight: 400;
    font-size: 102px;
    line-height: 1;
    letter-spacing: 0.01em;
    color: var(--title-gold);
    padding-left: 8px;
    box-sizing: border-box;
  }
  .wine-style {
    position: absolute;
    top: 458px;
    left: 0;
    width: 100%;
    margin: 0;
    text-align: center;
    font-family: "Barlow Semi Condensed", sans-serif;
    font-weight: 600;
    font-size: 46px;
    line-height: 1;
    letter-spacing: 0.33em;
    color: var(--ink-white);
    padding-left: 0.33em;
    box-sizing: border-box;
  }
  .landscape {
    position: absolute;
    top: 555px;
    left: 0;
    width: 826px;
    height: 368px;
    display: block;
  }
  .varietals {
    position: absolute;
    top: 982px;
    left: 0;
    width: 100%;
    margin: 0;
    padding: 0;
    list-style: none;
    text-align: center;
    font-family: "Barlow Semi Condensed", sans-serif;
    font-weight: 300;
    font-size: 36px;
    line-height: 40px;
    letter-spacing: 0.06em;
    color: var(--varietal-sand);
  }
  .varietals .divider {
    color: var(--divider-ink);
    font-weight: 600;
    font-size: 26px;
    margin: 0 6px;
    vertical-align: 3px;
  }
  .vintage {
    position: absolute;
    top: 1068px;
    left: 0;
    width: 100%;
    margin: 0;
    text-align: center;
    font-family: "Cormorant Garamond", serif;
    font-weight: 500;
    font-size: 36px;
    line-height: 1;
    letter-spacing: 0.12em;
    color: var(--ink-white);
  }
</style>
</head>
<body>
  <main class="wine-label">
    <h1 class="region-title">NAPA VALLEY</h1>
    <p class="wine-style">RED BLEND</p>

    <svg class="landscape" viewBox="0 0 826 368" role="img" aria-label="Illustration of rolling hills with a rising sun behind them and clusters of trees in the foreground">
      <defs>
        <linearGradient id="landscapeTone" x1="0" y1="0" x2="0" y2="1">
          <stop offset="0" stop-color="var(--label-stone)"/>
          <stop offset="0.35" stop-color="var(--landscape-mid)"/>
          <stop offset="0.7" stop-color="var(--landscape-mid)"/>
          <stop offset="1" stop-color="var(--landscape-dark)"/>
        </linearGradient>
      </defs>
      <rect x="0" y="0" width="826" height="368" fill="url(#landscapeTone)"/>
    </svg>

    <ul class="varietals">
      <li>MERLOT<span class="divider">|</span>CABERNET SAUVIGNON</li>
      <li>CABERNET FRANC<span class="divider">|</span>PETIT VERDOT<span class="divider">|</span>MALBEC</li>
    </ul>
    <p class="vintage">2018</p>
  </main>
</body>
</html>
```